Veltrano - Mechanic/Collision Center Business Card

We're looking for a business card design for our mechanic/ collision repair shop.

Can be with colours or monochromatic.

See the attached files.

Many thanks

```html
<!DOCTYPE html>
<html lang="pt">
<head>
<meta charset="utf-8">
<title>Veltrano – Business Card</title>
<link rel="stylesheet" href="https://fonts.googleapis.com/css2?family=Exo+2:wght@400;500;600;700;800&display=swap">
<style>
  :root {
    --backdrop: #d9d4cb;
    --card: #262626;
    --band: #1e1e1e;
    --brand-blue: #1e9ad6;
    --steel: #8a8d91;
    --text-light: #e6e6e6;
    --text-white: #ffffff;
  }
  * { box-sizing: border-box; margin: 0; padding: 0; }
  html, body {
    width: 1200px; height: 900px; overflow: hidden;
    background: var(--backdrop);
    font-family: "Exo 2", sans-serif;
  }
  .canvas { position: relative; width: 1200px; height: 900px; }

  .card {
    position: absolute; left: 311px; width: 577px; height: 329px;
    background: var(--card); overflow: hidden;
  }
  .card--front { top: 98px; }
  .card--back { top: 472px; }

  .tread-band { position: absolute; left: 0; width: 100%; height: 40px; background: var(--band); }
  .tread-band--top { top: 0; }
  .tread-band--bottom { bottom: 0; }
  .card--back .tread-band { height: 22px; }

  .brand { position: absolute; left: 0; width: 100%; text-align: center; }
  .brand__art {
    display: block; margin: 0 auto;
    background: linear-gradient(90deg, var(--steel) 0%, var(--brand-blue) 30%, var(--brand-blue) 70%, var(--steel) 100%);
    border-radius: 14px 14px 4px 4px;
  }
  .brand__name {
    display: block; color: var(--brand-blue); font-weight: 800;
    letter-spacing: 1px; line-height: 1;
  }
  .card--front .brand { top: 90px; }
  .card--front .brand__art { width: 221px; height: 87px; }
  .card--front .brand__name { font-size: 44px; margin-top: 10px; }
  .card--back .brand { top: 36px; }
  .card--back .brand__art { width: 190px; height: 77px; }
  .card--back .brand__name { font-size: 38px; margin-top: 5px; }

  .contact-person {
    position: absolute; right: calc(577px - 268px); top: 188px;
    text-align: right; color: var(--text-light);
  }
  .contact-person__name { font-size: 17px; font-weight: 700; color: var(--text-white); line-height: 22px; }
  .contact-person__role { font-size: 11px; color: var(--brand-blue); line-height: 14px; letter-spacing: .3px; }
  .contact-person__company { font-size: 14px; font-weight: 600; color: var(--brand-blue); line-height: 20px; margin-top: 5px; }
  .contact-person__address { font-size: 14px; line-height: 22px; }

  .divider { position: absolute; left: 287px; top: 193px; width: 2px; height: 95px; background: var(--brand-blue); }

  .contact-list { position: absolute; left: 307px; top: 190px; list-style: none; }
  .contact-list li {
    display: flex; align-items: center; height: 26px;
    font-size: 14.5px; color: var(--text-light);
  }
  .contact-list svg { width: 17px; height: 17px; margin-right: 6px; flex: none; fill: var(--brand-blue); }
  .social-square { width: 15px; height: 15px; background: var(--brand-blue); border-radius: 2px; margin: 0 8px 0 1px; flex: none; }
</style>
</head>
<body>
<main class="canvas">

  <section class="card card--front">
    <div class="tread-band tread-band--top"></div>
    <div class="brand">
      <span class="brand__art" role="img" aria-label="Illustration of three cars front-on with a wrench in the centre"></span>
      <span class="brand__name">VELTRANO</span>
    </div>
    <div class="tread-band tread-band--bottom"></div>
  </section>

  <section class="card card--back">
    <div class="tread-band tread-band--top"></div>
    <div class="brand">
      <span class="brand__art" role="img" aria-label="Illustration of three cars front-on with a wrench in the centre"></span>
      <span class="brand__name">VELTRANO</span>
    </div>

    <div class="contact-person">
      <p class="contact-person__name">RUI MATOS</p>
      <p class="contact-person__role">MANAGER</p>
      <p class="contact-person__company">Veltrano, LDA</p>
      <p class="contact-person__address">Rua das Oficinas, 42</p>
      <p class="contact-person__address">1900-214 Lisboa</p>
    </div>

    <div class="divider"></div>

    <ul class="contact-list">
      <li>
        <svg viewBox="0 0 24 24" aria-hidden="true"><path d="M6.6 10.8a15.1 15.1 0 0 0 6.6 6.6l2.2-2.2c.3-.3.7-.4 1-.2 1.1.4 2.3.6 3.6.6.6 0 1 .4 1 1V20c0 .6-.4 1-1 1A17 17 0 0 1 3 4c0-.6.4-1 1-1h3.5c.6 0 1 .4 1 1 0 1.3.2 2.5.6 3.6.1.3 0 .7-.2 1z"/></svg>
        +351 910482715
      </li>
      <li>
        <svg viewBox="0 0 24 24" aria-hidden="true"><path d="M8 2h8a2 2 0 0 1 2 2v16a2 2 0 0 1-2 2H8a2 2 0 0 1-2-2V4a2 2 0 0 1 2-2zm0 3v13h8V5zm4 14.2a.9.9 0 1 0 0 1.8.9.9 0 0 0 0-1.8z"/></svg>
        +351 213574026
      </li>
      <li>
        <svg viewBox="0 0 24 24" aria-hidden="true"><path d="M2 5h20v14H2zm2 2v.5l8 5.5 8-5.5V7l-8 5.2z"/></svg>
        veltrano.mail@example.com
      </li>
      <li>
        <span class="social-square"></span>
        veltrano
      </li>
    </ul>

    <div class="tread-band tread-band--bottom"></div>
  </section>

</main>
</body>
</html>
```